| 希望する色 | 特になし・その他 追記事項: 周囲の景色に埋没しないような色合いを希望します。 |
戸建賃貸住宅6棟の計画「ミドリテラス・カサネル」の看板デザインの依頼です。 【 概要 】 全6棟の戸建賃貸住宅を建築中です。 建築地が住宅街の中にあり場所がわかりにくいため、大通りから見える場所へ看板を掲出したいと考えています。 周辺にある戸建賃貸住宅は規格モノを建てただけですが、地元工務店と組んで自然環境を重視した計画としました。 賃貸住宅でも環境重視の方、都市部から郊外へ引っ越しをしてくる方、などにアピールしたいと思っています。 シンプルかつデザイン性の高い看板デザインを募集します。 【 依頼内容 】 ・看板サイズ:横3,000mm × 縦2,000mm ・看板の素材:メッシュターポリン(予定) ・デザイン素材:計画名のロゴは用意したものを使用してください。他はお任せします。 ・デザイン内容:「戸建賃貸住宅」は明示してください。建築地案内は矢印程度で良いかと考えています。敷地レイアウトの明示は不要です。 ・デザインの利用について:看板への使用が主目的ですが、HPへの掲載、不動産仲介業者への配布等も行う場合があります。作成デザインを尊重し編集、合成、切り抜き等は原則行いません。他制限事項あればお知らせください。 【 契約金額(税抜) 】 70,000円(税別) ※契約金額(税込)からシステム利用料を差し引いた金額が、ワーカーさまの受取金額となります その他ご質問等ありましたら、気軽にお問い合わせください。 ご応募をお待ちしております! |
| https://fuyoreside.sitelume.jp | ||
シンプルでもバランスが良く看板の目的に合致したデザインでした。
沢山のご提案ありがとうございました。良い案が幾つもあり採用デザインを1つに絞るのは悩みました。また機会がありましたらよろしくお願いします。

```html
<!DOCTYPE html>
<html lang="ja">
<head>
<meta charset="utf-8">
<title>ミドリテラス・カサネル 戸建賃貸住宅 看板</title>
<link rel="stylesheet" href="https://fonts.googleapis.com/css2?family=Noto+Sans+JP:wght@500;700;900&family=Zen+Maru+Gothic:wght@700&display=swap">
<style>
  :root {
    --page: #e9ebe8;
    --board: #ffffff;
    --ink: #1e1e1e;
    --green: #8cc43c;
    --muted: #3c3c3c;
    --band-text: #ffffff;
  }
  * { margin: 0; padding: 0; box-sizing: border-box; }
  html, body { width: 1200px; height: 814px; overflow: hidden; background: var(--page); }
  .signboard {
    position: absolute; left: 0; top: 7px;
    width: 1200px; height: 800px;
    background: var(--board);
    font-family: "Noto Sans JP", sans-serif;
    color: var(--ink);
  }
  .catch {
    position: absolute; left: 40px; top: 30px; width: 250px;
    font-family: "Zen Maru Gothic", sans-serif;
    font-weight: 700; line-height: 1;
  }
  .catch .char { display: block; }
  .catch .accent { color: var(--green); font-size: 104px; margin-bottom: 4px; }
  .catch .small { color: var(--muted); font-size: 62px; margin: 6px 0 10px 44px; }
  .scene {
    position: absolute; left: 300px; top: 0; width: 900px; height: 440px;
    background: linear-gradient(180deg, #eef3f6 0%, #dfe8e6 45%, #9cc068 70%, #6f9a44 100%);
  }
  .figures {
    position: absolute; left: 90px; top: 560px; width: 150px; height: 200px;
    background: linear-gradient(180deg, #3a3a3a, #1e1e1e);
    border-radius: 8px;
  }
  .band {
    position: absolute; left: 320px; top: 470px; width: 610px; height: 58px;
    background: var(--ink); color: var(--band-text);
    display: flex; align-items: center; justify-content: center;
    font-size: 28px; font-weight: 500; letter-spacing: 0.04em; white-space: nowrap;
  }
  .title {
    position: absolute; left: 320px; top: 548px; width: 610px;
    text-align: center; font-size: 88px; font-weight: 900; letter-spacing: 0.06em;
    line-height: 1.1; white-space: nowrap;
  }
  .name {
    position: absolute; left: 320px; top: 685px; width: 610px;
    text-align: center; font-size: 46px; font-weight: 700; line-height: 1.2;
    letter-spacing: 0.04em; white-space: nowrap;
  }
  .direction { position: absolute; left: 960px; top: 490px; width: 210px; height: 270px; }
</style>
</head>
<body>
  <main class="signboard">
    <div class="catch" aria-label="自然と遊ぶ">
      <span class="char accent">自然</span>
      <span class="char small">と</span>
      <span class="char accent">遊</span>
      <span class="char small">ぶ</span>
    </div>
    <div class="scene" role="img" aria-label="緑の木々に囲まれた白い戸建住宅が並ぶ街並みのイメージ"></div>
    <div class="figures" role="img" aria-label="手をつないで歩く親子のシルエット"></div>
    <div class="band">Midori Terrace Kasaneru</div>
    <div class="title">戸建賃貸住宅</div>
    <div class="name">ミドリテラス・カサネル</div>
    <svg class="direction" viewBox="0 0 210 270" aria-label="この先150m">
      <polygon points="105,0 210,95 210,270 0,270 0,95" fill="#1e1e1e"/>
      <text x="105" y="170" fill="#ffffff" font-family="Noto Sans JP, sans-serif" font-weight="900" font-size="64" text-anchor="middle">150<tspan font-size="40">m</tspan></text>
      <text x="105" y="235" fill="#ffffff" font-family="Noto Sans JP, sans-serif" font-weight="700" font-size="40" text-anchor="middle">この先</text>
    </svg>
  </main>
</body>
</html>
```